Calendar Ad / Flyer

Our law firm needs a calendar ad to place in a local calendar.
THE DEADLINE IS THIS THURSDAY 06/28/2018.

Attached is the ad used in last years calendar. A few notes on this...
**. This is by no means the model to follow.
Please be creative and do what makes more sense marketing wise.
1. Need to update the color scheme which corresponds to the new website at morvanlegal.net
2. The "MORVAN LEGAL | STANDING FIRM FOR YOUR FUTURE" should be put at the top and made larger
3. "KNOWN AND TRUSTED IN OUR COMMUNITY FOR OVER 21 YEARS" should be changed to "KNOWN AND TRUSTED IN OUR COMMUNITY FOR OVER 22 YEARS"
4. "Dorian K. Morvan, Esq." should be made larger and better positioned.
5. Under the list of practices, it should be changed to have:
"Personal Injury, Legal Malpractice, Unlicensed Contractors, Medical Malpractice, Civil Litigation"
6. Contact information (i.e. contact number, website, and address) should be better positioned
7. Placement of endorsement logos should stand out more.
8. New picture of head attorney is attached.

Last but not least... Give it your best shot!

```html
<!DOCTYPE html>
<html lang="en">
<head>
<meta charset="utf-8">
<title>Morvan Legal – Calendar Ad</title>
<link rel="stylesheet" href="https://fonts.googleapis.com/css2?family=Montserrat:wght@500&family=Open+Sans:wght@400;600;700;800&display=swap">
<style>
  :root {
    --page: #d6d6d6;
    --slate: #4a4d55;
    --slate-deep: #3e4148;
    --gold: #c9a66b;
    --gold-deep: #b8925a;
    --mist: #ececec;
    --paper: #ffffff;
    --ink: #3b3e45;
    --badge-blue: #1d5fa8;
    --badge-red: #8e1b1b;
    --badge-teal: #2a9fd6;
    --badge-rose: #d32323;
    --badge-bronze: #9c7a3c;
  }
  * { box-sizing: border-box; margin: 0; padding: 0; }
  html, body { width: 900px; height: 1200px; overflow: hidden; }
  body { background: var(--page); font-family: "Open Sans", sans-serif; position: relative; }

  .ad {
    position: absolute; left: 20px; top: 278px; width: 860px; height: 644px;
    background: var(--paper); overflow: hidden;
    box-shadow: 8px 10px 14px rgba(0,0,0,0.35);
  }
  .band { position: absolute; left: 0; width: 100%; }
  .band--brand { top: 0; height: 183px; background: var(--slate); }
  .band--headline { top: 183px; height: 110px; background: var(--mist); }
  .band--services { top: 293px; height: 84px; width: 560px; background: var(--slate); }
  .band--contact { top: 377px; height: 141px; background: var(--mist); }
  .band--rule { top: 518px; height: 6px; background: #d9d9d9; }
  .band--footer { top: 524px; height: 120px; background: var(--paper); }

  .brand { position: absolute; left: 27px; top: 34px; width: 480px; text-align: center; }
  .brand__name {
    display: inline-flex; align-items: center; gap: 14px;
    font-family: "Montserrat", sans-serif; font-weight: 500; font-size: 46px;
    letter-spacing: 3px; color: var(--gold); line-height: 1;
  }
  .brand__mark { width: 38px; height: 38px; background: var(--gold); }
  .brand__tagline {
    margin-top: 26px; font-size: 18px; color: #fff; letter-spacing: 0.5px; font-weight: 400;
  }

  .headline {
    position: absolute; left: 29px; top: 211px;
    font-weight: 800; font-size: 28px; line-height: 31px; color: var(--ink); letter-spacing: 0.3px;
  }
  .headline em { font-style: normal; color: var(--gold); }

  .services { position: absolute; left: 0; top: 293px; width: 560px; height: 84px; }
  .service {
    position: absolute; display: flex; align-items: center; gap: 6px;
    font-size: 15.5px; font-weight: 600; color: #fff; white-space: nowrap;
  }
  .service__dot { width: 12px; height: 12px; background: var(--gold); border-radius: 50%; }

  .toll-label {
    position: absolute; left: 187px; top: 395px; width: 136px; height: 22px;
    background: var(--gold); color: #fff; font-weight: 700; font-size: 16px;
    text-align: center; line-height: 22px;
  }
  .phone {
    position: absolute; left: 62px; top: 419px; width: 384px; height: 58px;
    background: var(--gold); box-shadow: 3px 3px 0 var(--gold-deep);
    display: flex; align-items: center; justify-content: center; gap: 12px;
  }
  .phone::after {
    content: ""; position: absolute; inset: 4px; border: 1.5px solid rgba(255,255,255,0.85);
  }
  .phone__number { font-size: 38px; font-weight: 600; color: #fff; letter-spacing: 0.5px; }
  .web {
    position: absolute; left: 146px; top: 482px; width: 214px; height: 26px;
    background: var(--slate); color: #fff; font-size: 14.5px;
    display: flex; align-items: center; justify-content: center; gap: 6px;
  }

  .attorney-photo {
    position: absolute; left: 539px; top: 19px; width: 306px; height: 436px;
    background: linear-gradient(180deg, #b9bcc1 0%, #8e9298 45%, #6f7379 100%);
  }
  .name-ribbon {
    position: absolute; left: 491px; top: 457px; width: 369px; height: 61px;
    background: var(--gold); clip-path: polygon(32px 0, 100% 0, 100% 100%, 0 100%);
    display: flex; align-items: center; justify-content: flex-end; padding-right: 22px;
    font-size: 26px; font-weight: 600; color: var(--ink);
  }

  .address {
    position: absolute; left: 30px; top: 562px; display: flex; gap: 8px;
    font-size: 14.5px; line-height: 20px; color: var(--ink);
  }
  .footer-divider { position: absolute; left: 290px; top: 535px; width: 1px; height: 99px; background: #bdbdbd; }
  .badge { position: absolute; }
  .badge--bureau { left: 318px; top: 566px; width: 94px; height: 33px; background: var(--badge-blue); border-radius: 3px; }
  .badge--forum { left: 438px; top: 550px; width: 66px; height: 66px; border-radius: 50%; background: var(--badge-red); border: 4px solid var(--gold); }
  .badge--rating { left: 532px; top: 548px; width: 74px; height: 74px; border-radius: 50%; background: #fff; border: 5px solid var(--badge-teal); }
  .badge--reviews { left: 645px; top: 558px; width: 80px; height: 52px; background: var(--badge-rose); border-radius: 4px; }
  .badge--peer { left: 750px; top: 556px; width: 84px; height: 58px; background: var(--badge-bronze); border-radius: 3px; }
</style>
</head>
<body>
  <main class="ad">
    <div class="band band--brand"></div>
    <div class="band band--headline"></div>
    <div class="band band--contact"></div>
    <div class="band band--services"></div>
    <div class="band band--rule"></div>
    <div class="band band--footer"></div>

    <header class="brand">
      <div class="brand__name"><span>MORVAN LEGAL</span><span class="brand__mark"></span></div>
      <p class="brand__tagline">STANDING FIRM FOR YOUR FUTURE</p>
    </header>

    <h1 class="headline">KNOWN AND TRUSTED IN OUR<br>COMMUNITY FOR OVER <em>22 YEARS</em></h1>

    <ul class="services" aria-label="Practice areas">
      <li class="service" style="left:27px;top:17px"><span class="service__dot"></span>Personal Injury</li>
      <li class="service" style="left:171px;top:17px"><span class="service__dot"></span>Legal Malpractice</li>
      <li class="service" style="left:336px;top:17px"><span class="service__dot"></span>Unlicensed Contractors</li>
      <li class="service" style="left:107px;top:53px"><span class="service__dot"></span>Medical Malpractice</li>
      <li class="service" style="left:300px;top:53px"><span class="service__dot"></span>Civil Litigation</li>
    </ul>

    <div class="toll-label">TOLL FREE:</div>
    <div class="phone">
      <svg width="34" height="34" viewBox="0 0 34 34" aria-hidden="true">
        <circle cx="17" cy="17" r="15" fill="none" stroke="#fff" stroke-width="2.5"/>
        <path d="M11 10.5c1-1 2.2-.8 2.8.2l1.5 2.5c.5.8.3 1.6-.4 2.2l-1 .8c.8 1.8 2.2 3.3 4 4.2l.9-1c.6-.7 1.5-.8 2.2-.3l2.5 1.6c.9.6 1 1.9.1 2.8l-1.3 1.2c-1 .9-2.6 1-4 .3-4-2-7-5-8.7-8.9-.6-1.4-.4-3 .6-4z" fill="#fff"/>
      </svg>
      <span class="phone__number">(888) 555-0142</span>
    </div>
    <div class="web">
      <svg width="13" height="13" viewBox="0 0 14 14" aria-hidden="true">
        <circle cx="7" cy="7" r="6" fill="none" stroke="#fff" stroke-width="1.3"/>
        <ellipse cx="7" cy="7" rx="2.6" ry="6" fill="none" stroke="#fff" stroke-width="1.1"/>
        <line x1="1" y1="7" x2="13" y2="7" stroke="#fff" stroke-width="1.1"/>
      </svg>
      <span>www.morvanlegal.net</span>
    </div>

    <div class="attorney-photo" role="img" aria-label="Portrait photograph of the head attorney standing in a grey suit with hands in pockets"></div>
    <div class="name-ribbon">Dorian K. Morvan, Esq.</div>

    <address class="address" style="font-style:normal">
      <svg width="14" height="18" viewBox="0 0 14 18" aria-hidden="true">
        <path d="M7 1a5.5 5.5 0 0 0-5.5 5.5C1.5 11 7 17 7 17s5.5-6 5.5-10.5A5.5 5.5 0 0 0 7 1z" fill="none" stroke="#555" stroke-width="1.3"/>
        <circle cx="7" cy="6.5" r="2" fill="none" stroke="#555" stroke-width="1.3"/>
      </svg>
      <span>2710 Larkspur Ave., Suite #304<br>Fairview, CA 90418</span>
    </address>
    <div class="footer-divider"></div>

    <div class="badge badge--bureau" role="img" aria-label="Business accreditation badge"></div>
    <div class="badge badge--forum" role="img" aria-label="Advocates forum membership seal"></div>
    <div class="badge badge--rating" role="img" aria-label="Attorney rating badge"></div>
    <div class="badge badge--reviews" role="img" aria-label="Customer reviews rating badge"></div>
    <div class="badge badge--peer" role="img" aria-label="Peer recognition award badge"></div>
  </main>
</body>
</html>
```